New website for a commercial real estate consulting company

What we’re looking for in a new web site:
• Desktop and mobile friendly
• Clear navigation
• Strong graphics
• Professional appearance
• The ability to update it ourselves
• Site is for information purposes only – no transactions required
• Traffic counts – number of visits per page?
• A firm quote on costs to develop and launch
• SSL
Attached is a copy of the revised text we propose to use, including our new logo. (The pagination can be different than as shown.)
Our current website address is www.brightlanecounselgroup.ca

```html
<!DOCTYPE html>
<html lang="en">
<head>
<meta charset="utf-8">
<title>Brightlane Counsel Group</title>
<link href="https://fonts.googleapis.com/css2?family=Cinzel:wght@400;600;700&family=Lato:ital,wght@0,400;0,700;1,700&display=swap" rel="stylesheet">
<style>
:root{
  --navy:#23267e;
  --navy-dark:#1b1d66;
  --ink:#2a2a2a;
  --text:#444;
  --grey-bg:#efefef;
  --light-bg:#f4f4f7;
  --footer:#1f1f1f;
  --white:#fff;
}
*{box-sizing:border-box;margin:0;padding:0}
html,body{width:1200px;height:4082px;overflow:hidden;background:var(--white)}
body{font-family:'Lato',sans-serif;color:var(--text);position:relative}
section,header,footer{position:absolute;left:0;width:1200px}
.abs{position:absolute}
.heading{font-family:'Cinzel',serif;font-weight:400;color:var(--ink);font-size:34px;letter-spacing:2px;text-align:center}
.rule{width:130px;height:3px;background:var(--navy);margin:18px auto 0}
.btn{display:inline-block;background:var(--navy);color:var(--white);font-family:'Cinzel',serif;font-weight:600;font-size:17px;letter-spacing:1px;border-radius:30px;padding:14px 38px}
.btn-outline{border:2px solid var(--navy);color:var(--navy);font-size:13px;font-weight:700;padding:12px 30px;display:inline-block}

/* header */
.site-header{top:0;height:140px;background:var(--white);z-index:3}
.brand{position:absolute;left:60px;top:-80px;width:260px;height:270px;border-radius:50%;background:var(--white);display:flex;flex-direction:column;align-items:center;justify-content:flex-end;padding-bottom:62px}
.brand-mark{width:40px;height:40px;background:var(--navy)}
.brand-name{font-family:'Cinzel',serif;color:var(--navy);font-size:17px;letter-spacing:1px;margin-top:8px;text-align:center;line-height:1.2}
.nav{position:absolute;right:70px;top:58px;display:flex;gap:46px;font-family:'Cinzel',serif;font-size:16px;letter-spacing:1px;color:var(--ink)}
.nav .active{color:var(--navy);font-weight:700}

/* hero */
.hero{top:140px;height:535px;background:linear-gradient(180deg,#3a4e68 0%,#28374d 45%,#1f2a3a 100%);z-index:1}
.hero-title{top:190px;width:100%;text-align:center;font-family:'Cinzel',serif;color:var(--white);font-size:54px;letter-spacing:3px}
.hero-sub{top:260px;width:100%;text-align:center;font-family:'Lato',sans-serif;font-weight:700;color:var(--white);font-size:28px;letter-spacing:2px}
.dots{top:488px;width:100%;display:flex;justify-content:center;gap:10px}
.dots span{width:14px;height:14px;border-radius:50%;border:2px solid var(--white)}
.dots .on{background:var(--white)}

/* welcome */
.welcome{top:675px;height:402px;text-align:center}
.welcome .heading{margin-top:55px}
.welcome p{width:1040px;margin:30px auto 0;font-size:15px;line-height:1.75}
.welcome .btn{margin-top:44px}

/* services */
.services{top:1077px;height:573px;background:var(--grey-bg)}
.services .heading{margin-top:42px}
.service{top:157px;width:250px}
.service-icon{width:80px;height:82px;background:linear-gradient(135deg,#c9cbe6,#8f93c8);border-radius:6px}
.service h3{font-family:'Cinzel',serif;font-weight:700;color:var(--ink);font-size:22px;margin-top:24px}
.service p{font-size:17px;line-height:1.35;margin-top:14px;height:142px}
.service .btn-outline{margin-top:10px}

/* team */
.team{top:1650px;height:758px}
.team .heading{margin-top:62px}
.member{top:167px;width:520px}
.member-photo{width:188px;height:240px;background:linear-gradient(160deg,#b7a79b,#6c5a52)}
.member-badge{position:absolute;left:188px;top:49px;width:320px;height:142px;background:var(--navy);clip-path:polygon(0 0,100% 0,94% 100%,0 100%);padding:28px 0 0 18px;color:var(--white)}
.member-badge h3{font-family:'Cinzel',serif;font-weight:600;font-size:21px;letter-spacing:1px;line-height:1.2}
.member-badge .cred{font-family:'Cinzel',serif;font-size:16px}
.member-badge .email{font-size:13px;font-weight:700;margin-top:14px}
.member p{font-size:15px;line-height:1.75;margin-top:24px}
.member .btn{margin-top:30px}

/* clients */
.clients{top:2408px;height:489px;background:var(--light-bg)}
.clients .heading{position:absolute;left:74px;top:62px;text-align:left}
.clients .rule{position:absolute;left:74px;top:118px;margin:0}
.client-list{position:absolute;top:168px;font-size:15px;line-height:1.35;list-style:none}
.client-list li{display:flex;align-items:flex-start;gap:12px;margin-bottom:26px;width:200px}
.client-list svg{flex:none;margin-top:1px}
.clients-photo{position:absolute;left:598px;top:0;width:602px;height:489px;background:linear-gradient(135deg,#b59272,#6e4a33 60%,#3a2a22)}

.quote-band{top:2897px;height:117px;background:var(--navy);color:var(--white);text-align:center;font-style:italic;font-weight:700;font-size:32px;padding-top:36px}

/* events */
.events{top:3014px;height:509px;background:var(--grey-bg)}
.events .heading{margin-top:48px}
.event{top:158px;width:320px}
.event-date{display:inline-block;border:2px solid #bdbdbd;background:var(--white);border-radius:30px;padding:6px 26px;font-family:'Cinzel',serif;font-size:15px;color:var(--ink)}
.event h3{font-family:'Cinzel',serif;font-weight:700;color:var(--navy);font-size:21px;margin-top:14px}
.event p{font-size:15px;line-height:1.5;margin-top:8px;color:var(--ink)}
.event .more{font-family:'Cinzel',serif;font-weight:700;color:var(--navy);font-size:13px;margin-top:14px;letter-spacing:1px}
.arrow{top:322px}
.events .view-all{position:absolute;top:405px;width:100%;text-align:center}

/* contact */
.contact{top:3523px;height:413px}
.contact .heading{position:absolute;left:74px;top:48px;text-align:left}
.contact .rule{position:absolute;left:74px;top:108px;margin:0}
.contact-info{position:absolute;left:74px;top:140px;font-size:14px;line-height:1.55;color:var(--ink)}
.contact-info .firm{font-family:'Cinzel',serif;color:var(--navy);font-weight:700;font-size:15px;margin-top:10px}
.contact-info .who{font-weight:700;margin-top:10px}
.contact-line{display:flex;align-items:center;gap:14px}
.contact-photo{position:absolute;left:615px;top:57px;width:511px;height:286px;background:linear-gradient(135deg,#8a6b50,#4b3a2e)}

/* footer */
.site-footer{top:3936px;height:146px;background:var(--footer);color:#ddd}
.footer-nav{position:absolute;left:74px;top:54px;display:flex;gap:34px;font-family:'Cinzel',serif;font-size:13px;letter-spacing:1px}
.copyright{position:absolute;left:74px;top:82px;font-size:12px;color:#999}
.social{position:absolute;right:80px;top:58px;display:flex;gap:18px}
.social span{width:22px;height:22px;border-radius:50%;background:#ddd}
</style>
</head>
<body>

<header class="site-header">
  <div class="brand">
    <div class="brand-mark"></div>
    <div class="brand-name">Brightlane<br>Counsel Group</div>
  </div>
  <nav class="nav">
    <span class="active">Home</span><span>Who We Are</span><span>What We Do</span><span>Contact Us</span><span>Industry Events Calendar</span>
  </nav>
</header>

<section class="hero" role="img" aria-label="Modern glass office building at dusk">
  <h1 class="abs hero-title">Brightlane Counsel Group</h1>
  <p class="abs hero-sub">EXPERT | EXPERIENCED | COST EFFECTIVE</p>
  <div class="abs dots"><span class="on"></span><span></span><span></span><span></span></div>
</section>

<section class="welcome">
  <h2 class="heading">Welcome to Our Website</h2>
  <div class="rule"></div>
  <p>Brightlane Counsel Group is an independent consulting firm offering practical, hands-on assistance to the commercial real estate and commercial mortgage lending industries. We specialize in financial analysis, underwriting and financial due diligence.<br>Working with us, you get top notch help when you need it – and only when you need it – one project at a time. Brightlane Counsel Group has been providing expert, experienced and cost-effective service to the commercial real estate and commercial mortgage industries since 2001. We have worked on projects across Canada and the United States, and in every major property type.</p>
  <span class="btn">Read More</span>
</section>

<section class="services">
  <h2 class="heading">What We Do</h2>
  <div class="rule"></div>
  <div class="abs service" style="left:65px">
    <div class="service-icon" role="img" aria-label="Owner icon"></div>
    <h3>For Owners</h3>
    <p>With sixty years of varied and progressive industry experience,<br>we have the expertise to quickly grasp the priorities</p>
    <span class="btn-outline">LEARN MORE</span>
  </div>
  <div class="abs service" style="left:356px">
    <div class="service-icon" role="img" aria-label="Key icon"></div>
    <h3>For Buyers</h3>
    <p>Our people have participated in transactions from all sides: as buyer, as vendor, as lender and as advisor, on deals</p>
    <span class="btn-outline">LEARN MORE</span>
  </div>
  <div class="abs service" style="left:637px">
    <div class="service-icon" role="img" aria-label="Lender with building icon"></div>
    <h3>For Lenders</h3>
    <p>Our people have participated in transactions from all sides: as buyer, as vendor, as lender and as advisor, on deals of $5</p>
    <span class="btn-outline">LEARN MORE</span>
  </div>
  <div class="abs service" style="left:917px">
    <div class="service-icon" role="img" aria-label="Broker icon"></div>
    <h3>For Brokers</h3>
    <p>Our people have participated in transactions from all sides: as buyer, as vendor, as lender and as advisor, on deals</p>
    <span class="btn-outline">LEARN MORE</span>
  </div>
</section>

<section class="team">
  <h2 class="heading">Who We Are</h2>
  <div class="rule"></div>
  <div class="abs member" style="left:76px">
    <div class="member-photo" role="img" aria-label="Portrait of Claire Donnelly"></div>
    <div class="member-badge">
      <h3>Claire Donnelly</h3>
      <div class="cred">MBA, MRICS</div>
      <div class="email">claire.donnelly@brightlanecounselgroup.ca</div>
    </div>
    <p>Claire has more than 30 years' senior experience in a wide range of property types. Her expertise encompasses all aspects of the financing, valuation, purchase and sale of commercial real estate. Prior to founding Brightlane Counsel Group in 2001, Claire spent 16 years of her career in a variety of institutional roles, culminating in ten years as Vice-President, Property Investments of a Canadian life insurance company.</p>
    <span class="btn">Read More</span>
  </div>
  <div class="abs member" style="left:615px">
    <div class="member-photo" role="img" aria-label="Portrait of Daniel Okafor" style="background:linear-gradient(160deg,#9aa0a8,#4a4f58)"></div>
    <div class="member-badge">
      <h3>Daniel Okafor,</h3>
      <div class="cred">AACI, MRICS</div>
      <div class="email">daniel.okafor@brightlanecounselgroup.ca</div>
    </div>
    <p>Daniel has more than 30 years' experience in all aspects of commercial real estate. He has designed and executed effective active asset management strategies on a Canada wide basis for both debt and equity portfolios. Daniel is also a fully accredited appraiser, and has provided valuation and consulting services throughout Ontario. Daniel's career has ranged over the entire real estate field....</p>
    <span class="btn">Read More</span>
  </div>
</section>

<section class="clients">
  <h2 class="heading">Our Clients Include</h2>
  <div class="rule"></div>
  <ul class="client-list" style="left:74px">
    <li><svg width="16" height="16" viewBox="0 0 16 16"><circle cx="8" cy="8" r="8" fill="#23267e"/><path d="M4.5 8.2l2.3 2.3 4.7-4.8" stroke="#fff" stroke-width="2" fill="none"/></svg>Chartered banks</li>
    <li><svg width="16" height="16" viewBox="0 0 16 16"><circle cx="8" cy="8" r="8" fill="#23267e"/><path d="M4.5 8.2l2.3 2.3 4.7-4.8" stroke="#fff" stroke-width="2" fill="none"/></svg>Mortgage bankers</li>
    <li><svg width="16" height="16" viewBox="0 0 16 16"><circle cx="8" cy="8" r="8" fill="#23267e"/><path d="M4.5 8.2l2.3 2.3 4.7-4.8" stroke="#fff" stroke-width="2" fill="none"/></svg>Public REITs &amp; REOCs</li>
    <li><svg width="16" height="16" viewBox="0 0 16 16"><circle cx="8" cy="8" r="8" fill="#23267e"/><path d="M4.5 8.2l2.3 2.3 4.7-4.8" stroke="#fff" stroke-width="2" fill="none"/></svg>Private equity firms</li>
    <li><svg width="16" height="16" viewBox="0 0 16 16"><circle cx="8" cy="8" r="8" fill="#23267e"/><path d="M4.5 8.2l2.3 2.3 4.7-4.8" stroke="#fff" stroke-width="2" fill="none"/></svg>Family-owned real estate investment companies</li>
  </ul>
  <ul class="client-list" style="left:314px">
    <li><svg width="16" height="16" viewBox="0 0 16 16"><circle cx="8" cy="8" r="8" fill="#23267e"/><path d="M4.5 8.2l2.3 2.3 4.7-4.8" stroke="#fff" stroke-width="2" fill="none"/></svg>Life insurance companies</li>
    <li><svg width="16" height="16" viewBox="0 0 16 16"><circle cx="8" cy="8" r="8" fill="#23267e"/><path d="M4.5 8.2l2.3 2.3 4.7-4.8" stroke="#fff" stroke-width="2" fill="none"/></svg>Pension funds</li>
    <li><svg width="16" height="16" viewBox="0 0 16 16"><circle cx="8" cy="8" r="8" fill="#23267e"/><path d="M4.5 8.2l2.3 2.3 4.7-4.8" stroke="#fff" stroke-width="2" fill="none"/></svg>Non-bank lenders</li>
    <li><svg width="16" height="16" viewBox="0 0 16 16"><circle cx="8" cy="8" r="8" fill="#23267e"/><path d="M4.5 8.2l2.3 2.3 4.7-4.8" stroke="#fff" stroke-width="2" fill="none"/></svg>Brokerage firms</li>
  </ul>
  <div class="clients-photo" role="img" aria-label="Team members joining hands in a high five"></div>
</section>

<section class="quote-band">“Reputation is the currency of the 21 st century”</section>

<section class="events">
  <h2 class="heading">Industry Events Calendar</h2>
  <div class="rule"></div>
  <svg class="abs arrow" style="left:40px" width="22" height="36" viewBox="0 0 22 36"><path d="M18 3L4 18l14 15" stroke="#444" stroke-width="5" fill="none"/></svg>
  <svg class="abs arrow" style="left:1138px" width="22" height="36" viewBox="0 0 22 36"><path d="M4 3l14 15L4 33" stroke="#444" stroke-width="5" fill="none"/></svg>
  <div class="abs event" style="left:87px">
    <span class="event-date">January 2019</span>
    <h3>27-29 Pacific Retail Forum</h3>
    <p>Fusce finibus nunc diam, ut efficitur massa interdum interdum. Nulla ullamcorper mattis dui a rhoncus.</p>
    <div class="more">READ MORE</div>
  </div>
  <div class="abs event" style="left:443px">
    <span class="event-date">February 2019</span>
    <h3>26 Capital Markets Summit</h3>
    <p>Fusce finibus nunc diam, ut efficitur massa interdum interdum. Nulla ullamcorper mattis dui a rhoncus.</p>
    <div class="more">READ MORE</div>
  </div>
  <div class="abs event" style="left:805px">
    <span class="event-date">March 2019</span>
    <h3>6 Women in Property AGM</h3>
    <p>Fusce finibus nunc diam, ut efficitur massa interdum interdum. Nulla ullamcorper mattis dui a rhoncus.</p>
    <div class="more">READ MORE</div>
  </div>
  <div class="view-all"><span class="btn">View All Events</span></div>
</section>

<section class="contact">
  <h2 class="heading">Contact Us</h2>
  <div class="rule"></div>
  <div class="contact-info">
    <p>To discuss your real estate needs in confidence, please contact:</p>
    <p class="firm">BRIGHTLANE COUNSEL GROUP</p>
    <p>418 Maple Ridge Road Milton,<br>Ontario L9K 2T4</p>
    <p class="who">Claire Donnelly</p>
    <p class="contact-line"><svg width="14" height="14" viewBox="0 0 14 14"><path d="M3 1l2.5 3-1.5 1.5c.8 1.8 2.2 3.2 4 4L9.5 8l3 2.5-1.5 2.5C6 13 1 8 1 2.5z" fill="#333"/></svg>905.555.0142</p>
    <p class="contact-line"><svg width="14" height="14" viewBox="0 0 14 14"><rect x="3.5" y="0.5" width="7" height="13" rx="1.5" fill="#333"/><rect x="5" y="2.5" width="4" height="8" fill="#fff"/></svg>905.555.0187</p>
    <p class="contact-line"><svg width="14" height="14" viewBox="0 0 14 14"><rect x="0.5" y="2.5" width="13" height="9" fill="#333"/><path d="M1 3l6 5 6-5" stroke="#fff" fill="none"/></svg>claire.donnelly@brightlanecounselgroup.ca</p>
  </div>
  <div class="contact-photo" role="img" aria-label="Laptop and coffee cup on a wooden desk"></div>
</section>

<footer class="site-footer">
  <nav class="footer-nav"><span>Home</span><span>Who We Are</span><span>What We Do</span><span>Contact Us</span><span>Industry Events Calendar</span></nav>
  <p class="copyright">Copyright © 2019. Company Name. All Rights Reserved.</p>
  <div class="social" aria-label="Social media links"><span></span><span></span><span></span><span></span></div>
</footer>

</body>
</html>
```